Pharmaceutical Manufacturing Services Advertisement

We need a new full page advertisement designed for publication in international magazines. We are a custom pharmaceutical manufacturing company and we help biotechnology companies scale up their drug development for clinical trials. The products we help manufacture are therapeutics for global healthcare problems.

Target Market(s)

Verott Bio is a privately owned contract development manufacturing organisation (CDMO) headquartered in Darra, QLD, Australia.

Our mission is to is to be a global leader in development and in the provision of contract manufacturing for active pharmaceutical ingredient processes.

Why we do what we Do:

To help advance Biotechnology Companies so that they can deliver innovative therapeutics
~ enabling patients to live longer, healthier and happier lives
~ which solves worldwide health problems

Verott Bio’s role is to develop, implement and scale up the production to deliver biologic medicines for patients in partnership with the biotechnology companies.

Industry/Entity Type

Biotechnology

Font styles to use
Sans Serif

Colors

Designer to choose colors to be used in the design.

Requirements
Must have
• Please see the script on the Word document. There are 4 optional Header Taglines. Additional ideas for multiple designs for the taglines welcomed.
• However preference is for either of the first two:
• 1. Building your vision for better healthcare
• 2. Bridging your vision for better healthcare
• File Specs:
• • All artwork should be submitted as high-resolution (300 min. dpi), press-ready PDF files
• • CMYK color only
• • Full page 8.25” x 10.812”; 209.55 x 274.62 mm
• • Live Area for all sizes: 0.25” (6.35 mm) inside the trim
• • Bleed Area for all sizes: Extends 0.125” (3.175 mm) from trim
Nice to have
• Modern Science look to inspire biotechnology companies to work with us.
• Search for images to use by keyword "recombinant dna"

```html
<!DOCTYPE html>
<html lang="en">
<head>
<meta charset="utf-8">
<title>Verott Bio – Building Your Vision for Better Healthcare</title>
<link rel="stylesheet" href="https://fonts.googleapis.com/css2?family=Oswald:wght@400;500&family=Open+Sans:wght@400;600;700&display=swap">
<style>
  :root {
    --green: #b4bc33;
    --navy: #173e5c;
    --navy-band: rgba(23, 62, 92, 0.92);
    --text-grey: #4b4b4d;
    --page-bg: #ffffff;
    --canvas-bg: #e6e6e6;
    --white: #ffffff;
  }
  html, body {
    margin: 0;
    padding: 0;
    width: 998px;
    height: 1200px;
    overflow: hidden;
    background: var(--canvas-bg);
  }
  .ad-page {
    position: absolute;
    left: 56px;
    top: 0;
    width: 886px;
    height: 1200px;
    background: var(--page-bg);
    overflow: hidden;
    font-family: "Open Sans", Arial, sans-serif;
  }
  .hero-photo {
    position: absolute;
    left: 0;
    top: 149px;
    width: 886px;
    height: 420px;
    background:
      radial-gradient(ellipse 180px 230px at 74% 52%, rgba(190, 214, 240, 0.85), rgba(190, 214, 240, 0) 70%),
      linear-gradient(90deg, #6f6a3c 0%, #c9b678 14%, #b9a66a 26%, #3f6f93 40%, #2f6a99 60%, #4b87bd 80%, #2b5f8c 100%);
  }
  .headline-box {
    position: absolute;
    left: 30px;
    top: 0;
    width: 346px;
    height: 322px;
    background: var(--green);
    border-radius: 0 0 10px 10px;
    z-index: 2;
  }
  .headline {
    position: absolute;
    left: 38px;
    top: 100px;
    margin: 0;
    font-family: "Oswald", "Arial Narrow", sans-serif;
    font-weight: 500;
    font-size: 37px;
    line-height: 54px;
    color: var(--white);
    text-transform: uppercase;
  }
  .brand {
    position: absolute;
    left: 602px;
    top: 62px;
    width: 270px;
  }
  .brand-name {
    margin: 0;
    font-family: "Open Sans", Arial, sans-serif;
    font-weight: 700;
    font-size: 44px;
    line-height: 52px;
    color: var(--navy);
    letter-spacing: 0.5px;
    white-space: nowrap;
  }
  .brand-tagline {
    margin: 6px 0 0;
    font-family: "Oswald", "Arial Narrow", sans-serif;
    font-size: 15px;
    color: var(--navy);
    letter-spacing: 0.3px;
    text-transform: uppercase;
  }
  .partner-band {
    position: absolute;
    left: 0;
    top: 555px;
    width: 886px;
    height: 84px;
    background: var(--navy-band);
    border-bottom-right-radius: 70px 40px;
    display: flex;
    align-items: center;
  }
  .partner-band h2 {
    margin: 0 0 0 45px;
    font-family: "Open Sans", Arial, sans-serif;
    font-weight: 600;
    font-size: 23px;
    color: var(--white);
    text-transform: uppercase;
  }
  .intro {
    position: absolute;
    left: 45px;
    top: 672px;
    width: 796px;
    color: var(--text-grey);
    font-size: 16px;
    line-height: 23px;
  }
  .intro p { margin: 0 0 23px; }
  .offer-panel {
    position: absolute;
    top: 868px;
    height: 210px;
    background: var(--green);
    border-radius: 10px;
    overflow: hidden;
  }
  .offer-panel.products { left: 45px; width: 389px; }
  .offer-panel.services { left: 444px; width: 397px; }
  .offer-panel h3 {
    margin: 0;
    height: 52px;
    line-height: 52px;
    background: var(--navy);
    color: var(--white);
    text-align: center;
    font-size: 21px;
    font-weight: 600;
    text-transform: uppercase;
  }
  .offer-list {
    list-style: none;
    margin: 14px 0 0;
    padding: 0 0 0 20px;
  }
  .offer-list li {
    display: flex;
    align-items: center;
    gap: 12px;
    color: var(--white);
    font-size: 15.5px;
    line-height: 27px;
    white-space: nowrap;
  }
  .bullet { flex: none; width: 13px; height: 13px; }
  .call-bar {
    position: absolute;
    left: 45px;
    top: 1098px;
    width: 796px;
    height: 50px;
    background: var(--navy);
    border-radius: 25px;
    display: flex;
    align-items: center;
    justify-content: center;
    gap: 18px;
    color: var(--white);
    font-weight: 700;
    font-size: 21px;
    box-shadow: 0 4px 8px rgba(0, 0, 0, 0.25);
  }
  .call-bar svg { width: 22px; height: 22px; }
  .call-number { font-weight: 600; margin-left: 6px; }
  .contact-line {
    position: absolute;
    left: 0;
    top: 1160px;
    width: 886px;
    margin: 0;
    text-align: center;
    color: var(--text-grey);
    font-size: 18px;
    font-weight: 600;
  }
</style>
</head>
<body>
<main class="ad-page">
  <div class="hero-photo" role="img" aria-label="Photograph of a scientist in a hairnet and safety glasses working beside fermentation columns in a clean-room laboratory"></div>

  <div class="headline-box">
    <h1 class="headline">Building your<br>vision for better<br>healthcare</h1>
  </div>

  <div class="brand">
    <p class="brand-name">VEROTT BIO</p>
    <p class="brand-tagline">Biopharmaceutical Manufacturing</p>
  </div>

  <div class="partner-band">
    <h2>Your partner in early phase clinical biomanufacturing</h2>
  </div>

  <section class="intro">
    <p>We have been serving the pharmaceutical, biotechnology and veterinary industry for over 20 years so you can create innovative medicines for worldwide health problems.</p>
    <p>Get your therapeutics to the patient faster with cost-effective manufacturing for your GMP clinical trial material. We offer rapid technology transfer, scale-up development and manufacturing of microbial cell-derived proteins at up to 500L scale. We prepare your active pharmaceutical ingredient (API) products to a world class standard ready for clinical development.</p>
  </section>

  <section class="offer-panel products">
    <h3>Products</h3>
    <ul class="offer-list">
      <li><svg class="bullet" viewBox="0 0 13 13"><circle cx="6.5" cy="6.5" r="6.5" fill="#173e5c"/><path d="M5 3.8 L7.8 6.5 L5 9.2" stroke="#fff" stroke-width="1.6" fill="none"/></svg>Recombinant proteins</li>
      <li><svg class="bullet" viewBox="0 0 13 13"><circle cx="6.5" cy="6.5" r="6.5" fill="#173e5c"/><path d="M5 3.8 L7.8 6.5 L5 9.2" stroke="#fff" stroke-width="1.6" fill="none"/></svg>Live Biotherapeutics</li>
      <li><svg class="bullet" viewBox="0 0 13 13"><circle cx="6.5" cy="6.5" r="6.5" fill="#173e5c"/><path d="M5 3.8 L7.8 6.5 L5 9.2" stroke="#fff" stroke-width="1.6" fill="none"/></svg>Bacterial vaccines</li>
      <li><svg class="bullet" viewBox="0 0 13 13"><circle cx="6.5" cy="6.5" r="6.5" fill="#173e5c"/><path d="M5 3.8 L7.8 6.5 L5 9.2" stroke="#fff" stroke-width="1.6" fill="none"/></svg>Plasmid DNA</li>
    </ul>
  </section>

  <section class="offer-panel services">
    <h3>Services</h3>
    <ul class="offer-list">
      <li><svg class="bullet" viewBox="0 0 13 13"><circle cx="6.5" cy="6.5" r="6.5" fill="#173e5c"/><path d="M5 3.8 L7.8 6.5 L5 9.2" stroke="#fff" stroke-width="1.6" fill="none"/></svg>Bacterial / Yeast Fermentation</li>
      <li><svg class="bullet" viewBox="0 0 13 13"><circle cx="6.5" cy="6.5" r="6.5" fill="#173e5c"/><path d="M5 3.8 L7.8 6.5 L5 9.2" stroke="#fff" stroke-width="1.6" fill="none"/></svg>Cell Banking</li>
      <li><svg class="bullet" viewBox="0 0 13 13"><circle cx="6.5" cy="6.5" r="6.5" fill="#173e5c"/><path d="M5 3.8 L7.8 6.5 L5 9.2" stroke="#fff" stroke-width="1.6" fill="none"/></svg>Process Development/Scale-up</li>
      <li><svg class="bullet" viewBox="0 0 13 13"><circle cx="6.5" cy="6.5" r="6.5" fill="#173e5c"/><path d="M5 3.8 L7.8 6.5 L5 9.2" stroke="#fff" stroke-width="1.6" fill="none"/></svg>cGMP Manufacture of biopharmaceutical APIs</li>
      <li><svg class="bullet" viewBox="0 0 13 13"><circle cx="6.5" cy="6.5" r="6.5" fill="#173e5c"/><path d="M5 3.8 L7.8 6.5 L5 9.2" stroke="#fff" stroke-width="1.6" fill="none"/></svg>Stability Testing</li>
    </ul>
  </section>

  <div class="call-bar">
    <span>TAKE THE FIRST STEP - CALL US TODAY!</span>
    <svg viewBox="0 0 24 24" aria-hidden="true">
      <circle cx="12" cy="12" r="10.5" fill="none" stroke="#fff" stroke-width="1.8"/>
      <path d="M8.6 6.8c.4-.3 1-.2 1.2.2l1 1.9c.2.4.1.8-.2 1.1l-.7.6c.5 1.2 1.4 2.1 2.6 2.7l.6-.7c.3-.3.7-.4 1.1-.2l1.9 1c.4.2.5.8.2 1.2l-.8 1c-.5.6-1.3.8-2 .5-2.7-1.1-4.7-3.1-5.8-5.8-.3-.7-.1-1.5.5-2z" fill="#fff"/>
    </svg>
    <span class="call-number">+61(7)35550142</span>
  </div>

  <p class="contact-line">Visit verottbio.com.au | enquiries@verottbio.com.au</p>
</main>
</body>
</html>
```